Ecommerce website Home Page Design that is clean and elegant

Design a Home page for an ecommerce website. This website products and offerings will be very similar to :

brightmeadowtrinkets.com
pebblelanegoods.com

Target Market(s)

Consumer and small shops who can order online.

Industry/Entity Type

Retail

Number of Pages Required

1 page

Colors

Designer to choose colors to be used in the design.

Requirements
Must have
• Exact competition with similar products:
• brightmeadowtrinkets.com
• http://www.pebblelanegoods.com/
• Home page with featured image banner
• List of items on sale or category based items list
• atleast three banners for sale or shipping related offers.
Nice to have
• The logo has very light colors and products will have lots of colors as you can see on competition sites. So the design must consider this so that logo also stands out somewhat for branding purpose.
Should not have
• Design should not have black background

```html
<!DOCTYPE html>
<html lang="en">
<head>
<meta charset="utf-8">
<title>Partyvale – Home</title>
<link href="https://fonts.googleapis.com/css2?family=Open+Sans:wght@300;400;600;700&family=Roboto:wght@300;400;500;700&display=swap" rel="stylesheet">
<style>
:root{
  --teal:#4c9ea9;
  --teal-dark:#3c8792;
  --orange:#f2a52e;
  --pink:#ef8fa3;
  --nav:#3a3d40;
  --ink:#333;
  --muted:#888;
  --line:#e2e2e2;
  --grey-bg:#efefef;
  --white:#fff;
}
*{box-sizing:border-box;margin:0;padding:0}
html,body{width:1200px;height:3512px;overflow:hidden}
body{font-family:"Open Sans",Arial,sans-serif;color:var(--ink);background:var(--white);position:relative}
a{color:inherit;text-decoration:none}
.btn{display:inline-block;background:var(--teal);color:#fff;font-size:15px;font-weight:600;padding:10px 26px;border-radius:2px;white-space:nowrap}
.wrap{width:1040px;margin:0 auto;position:relative}

/* top bar */
.topbar{height:32px;border-bottom:1px solid var(--line);font-size:12px;color:var(--muted)}
.topbar .wrap{display:flex;justify-content:space-between;align-items:center;height:32px}
.topbar .links{white-space:nowrap}
.topbar .links span{margin-right:14px}
.topbar .links .hl{color:var(--orange)}
.login{background:var(--teal);color:#fff;padding:0 14px;height:32px;line-height:32px}

/* header */
.header{height:88px}
.header .wrap{display:flex;align-items:center;height:88px;justify-content:space-between}
.brand{display:flex;align-items:center;gap:10px;font-family:"Roboto",sans-serif;font-size:40px;font-weight:700;color:var(--teal);letter-spacing:-.5px;white-space:nowrap}
.brand .dot{width:16px;height:16px;border-radius:50%;background:var(--orange)}
.search{display:flex;width:360px;height:40px;border:1px solid #ccc}
.search .field{flex:1;padding:0 14px;line-height:38px;color:#aaa;font-size:14px}
.search .go{width:44px;background:var(--orange);display:flex;align-items:center;justify-content:center}
.callus{font-size:17px;color:var(--ink);white-space:nowrap}
.callus b{color:var(--teal)}
.cart{width:40px;height:40px;border:2px solid var(--teal);border-radius:50%;display:flex;align-items:center;justify-content:center;margin-left:16px}

/* nav */
.nav{height:48px;background:var(--nav)}
.nav .wrap{display:flex;height:48px;align-items:center}
.nav a{color:#fff;font-size:14px;padding:0 15px;line-height:48px;white-space:nowrap}
.nav a.active{background:var(--orange)}

/* hero */
.hero{height:344px;position:relative;background:linear-gradient(180deg,#bcd4e2 0%,#cfdfe6 45%,#d9cdb7 75%,#e6d8c2 100%)}
.hero-card{position:absolute;left:150px;top:64px;width:400px;height:196px;border:2px solid rgba(255,255,255,.9);padding:24px 30px;color:#fff;white-space:nowrap}
.hero-card .kicker{font-size:17px}
.hero-card h1{font-family:"Roboto",sans-serif;font-weight:300;font-size:56px;line-height:1.05;margin:4px 0 2px}
.hero-card .sub{font-size:22px;font-weight:300}
.hero-card .btn{position:absolute;left:30px;bottom:-18px;background:var(--orange);font-size:13px;padding:8px 22px}
.arrow{position:absolute;top:156px;width:30px;height:30px;border-radius:50%;background:rgba(255,255,255,.85);display:flex;align-items:center;justify-content:center}
.arrow.l{left:10px}.arrow.r{right:10px}

/* promos */
.promos{padding:120px 0 0;height:632px}
.promo-grid{display:grid;grid-template-columns:260px 260px 492px;grid-template-rows:252px 252px;column-gap:0;width:1040px;margin:0 auto;position:relative}
.promo-grid .big{grid-column:3;grid-row:1/3;margin-left:20px;position:relative}
.tile{position:relative;padding:40px 30px;color:#fff}
.tile.pink{background:var(--pink)}
.tile.teal{background:var(--teal)}
.tile .tag{font-size:12px;letter-spacing:1px;text-transform:uppercase;border-bottom:1px solid rgba(255,255,255,.7);padding-bottom:8px;display:inline-block}
.tile h3{font-size:26px;font-weight:400;line-height:1.2;margin:14px 0 20px}
.tile .btn{background:#fff;color:var(--ink);font-size:12px;padding:7px 18px}
.ph{display:block;width:100%;height:100%}
.big-label{position:absolute;right:0;top:90px;width:280px;padding:30px;background:rgba(60,135,146,.85);color:#fff}
.big-label .tag{font-size:12px;letter-spacing:1px;text-transform:uppercase}
.big-label h3{font-size:38px;font-weight:300;margin:6px 0;white-space:nowrap}
.big-label p{font-size:20px}

/* categories */
.categories{background:var(--grey-bg);height:576px;padding-top:48px}
.sec-title{font-size:26px;font-weight:400;display:flex;align-items:center;gap:14px;white-space:nowrap}
.sec-title b{font-weight:700}
.sec-title .rule{height:2px;width:120px;background:var(--teal)}
.cat-wrap{display:flex;gap:32px;margin-top:24px}
.cat-feature{width:308px;height:396px;border:2px solid var(--teal);background:#fff;position:relative;padding:40px 16px 16px}
.cat-feature .name{position:absolute;top:10px;left:0;right:0;text-align:center;font-size:15px}
.cat-grid{display:grid;grid-template-columns:repeat(3,212px);grid-template-rows:176px 176px;gap:32px 28px}
.cat{position:relative;background:#fff}
.cat .label{position:absolute;left:0;bottom:14px;background:var(--teal);color:#fff;font-size:14px;padding:5px 14px;white-space:nowrap}

/* banners */
.banners{height:480px;padding-top:116px}
.banners .wrap{display:flex;gap:36px}
.banner{flex:1;height:308px;position:relative}
.banner .label{position:absolute;left:0;bottom:22px;color:#fff;padding:8px 18px;min-width:300px}
.banner .label b{display:block;font-size:17px}
.banner .label span{font-size:11px}
.banner .label.teal{background:var(--teal)}
.banner .label.orange{background:var(--orange)}

/* featured */
.featured{height:440px;padding-top:48px}
.featured .head{display:flex;justify-content:space-between;align-items:center}
.featured .head .rule{width:220px}
.dots{display:flex;gap:6px;align-items:center}
.dots span{width:22px;height:22px;border-radius:50%;border:2px solid var(--orange)}
.dots span.on{background:var(--orange)}
.products{display:flex;gap:32px;margin-top:30px}
.product{width:236px;height:320px;border:1px solid var(--line);padding:12px;text-align:left;background:#fff}
.product .img{height:164px}
.product h4{font-size:13px;font-weight:400;margin:12px 0 6px;line-height:1.35;height:36px}
.price{font-size:14px}
.price s{color:var(--muted);margin-right:6px}
.price b{color:var(--orange);font-weight:600}
.product .btn{margin-top:14px;font-size:13px;padding:8px 20px}

/* shipping */
.shipping{height:420px;position:relative;overflow:hidden}
.shipping svg.bg{position:absolute;inset:0}
.ship-text{position:relative;text-align:center;padding-top:36px}
.ship-text h2{font-size:40px;font-weight:600;color:var(--teal)}
.ship-text p{font-size:17px;margin:8px 0 20px}
.features{position:absolute;left:80px;right:80px;top:200px;display:flex;background:#fff;box-shadow:0 2px 10px rgba(0,0,0,.08)}
.feature{flex:1;text-align:center;padding:24px 40px 26px;border-right:1px solid var(--line)}
.feature:last-child{border-right:0}
.feature h5{font-size:15px;font-weight:700;margin:10px 0 8px}
.feature p{font-size:12px;color:var(--muted);line-height:1.5}

/* footer */
.footer{background:var(--teal);height:440px;color:#fff;padding-top:32px;position:relative}
.footer .wrap{display:flex;gap:70px}
.footer .col{flex:1}
.footer .brand{color:#fff;font-size:36px}
.footer p{font-size:13px;line-height:1.6;margin-top:12px}
.footer h6{font-size:17px;font-weight:600;border-bottom:1px solid rgba(255,255,255,.5);padding-bottom:10px;margin-bottom:14px}
.footer .btn{background:#fff;color:var(--teal);margin-top:20px;font-size:13px}
.contact-line{font-size:13px;margin-bottom:10px;display:flex;gap:8px;align-items:center}
.newsletter{display:flex;flex-direction:column;gap:12px;margin-top:14px}
.newsletter .field{background:#fff;color:#aaa;height:36px;line-height:36px;padding:0 12px;font-size:13px}
.newsletter .btn{margin-top:0;align-self:flex-start;background:var(--orange);color:#fff}
.bottombar{position:absolute;left:0;right:0;bottom:0;height:70px;background:#fff;border-top:4px solid var(--orange)}
.bottombar .wrap{display:flex!important;gap:0!important;justify-content:space-between;align-items:center;height:66px;font-size:12px;color:var(--muted);white-space:nowrap}
.bottombar nav{font-size:12px}
.bottombar nav a{margin:0 8px;color:var(--ink)}
.bottombar nav a.active{color:var(--orange)}
.up{width:34px;height:34px;border-radius:50%;background:var(--orange);display:flex;align-items:center;justify-content:center}
</style>
</head>
<body>

<div class="topbar"><div class="wrap">
  <div class="links"><span>About Us</span><span class="hl">Customer Service</span><span>Help &amp; FAQ</span><span>Return Policy</span><span>Shipping Information</span><span>Contact Us</span></div>
  <div class="login">Login</div>
</div></div>

<header class="header"><div class="wrap">
  <div class="brand"><span class="dot"></span>Partyvale</div>
  <div class="search"><div class="field">Search...</div><div class="go">
    <svg width="18" height="18" viewBox="0 0 18 18"><circle cx="7.5" cy="7.5" r="5.5" fill="none" stroke="#fff" stroke-width="2"/><line x1="11.5" y1="11.5" x2="16" y2="16" stroke="#fff" stroke-width="2"/></svg></div></div>
  <div style="display:flex;align-items:center">
    <div class="callus">Call Us <b>(555)-014-7890</b></div>
    <div class="cart"><svg width="20" height="18" viewBox="0 0 20 18"><path d="M1 2h3l2 9h10l2-7H5" fill="none" stroke="#4c9ea9" stroke-width="2"/><circle cx="8" cy="15" r="1.6" fill="#4c9ea9"/><circle cx="15" cy="15" r="1.6" fill="#4c9ea9"/></svg></div>
  </div>
</div></header>

<nav class="nav"><div class="wrap">
  <a class="active">Home</a><a>Party Supplies</a><a>Occasions &amp; Events</a><a>Toys &amp; Games</a><a>Crafts</a><a>Teacher Supplies</a><a>Wedding</a><a>Holidays</a><a>Sale</a>
</div></nav>

<section class="hero" role="img" aria-label="Woman in a swimsuit and sun hat sitting on a sunny beach">
  <div class="hero-card">
    <div class="kicker">Summer Fun with <b>Super Savings!</b></div>
    <h1>Summer Wear</h1>
    <div class="sub">Sale Up to <b>50%</b> off</div>
    <a class="btn">Shop Now</a>
  </div>
  <div class="arrow l"><svg width="10" height="12"><path d="M8 1L2 6l6 5" fill="none" stroke="#333" stroke-width="2"/></svg></div>
  <div class="arrow r"><svg width="10" height="12"><path d="M2 1l6 5-6 5" fill="none" stroke="#333" stroke-width="2"/></svg></div>
</section>

<section class="promos">
  <div class="promo-grid">
    <div class="ph" role="img" aria-label="Colourful glow sticks and bracelets" style="background:linear-gradient(135deg,#2a1f4a,#7b3fa0 45%,#3fb6c9)"></div>
    <div class="tile pink"><span class="tag">Party Supplies</span><h3>Sports Party Supplies</h3><a class="btn">Shop Now</a></div>
    <div class="big">
      <div class="ph" role="img" aria-label="Light-up party mug glowing in rainbow colours" style="background:linear-gradient(135deg,#1d2233,#3a4a6a 50%,#c48a3a)"></div>
      <div class="big-label"><div class="tag">Best Offer</div><h3>Up to <b>70% Off</b></h3><p>Clearance Sale</p></div>
    </div>
    <div class="tile teal"><span class="tag">Toys &amp; Games</span><h3>Fidget Spinners &amp; Fidget Toys</h3><a class="btn">Shop Now</a></div>
    <div class="ph" role="img" aria-label="Bundle of neon glow sticks" style="background:linear-gradient(135deg,#1b1b2e,#c43a8a 50%,#f2d13a)"></div>
  </div>
</section>

<section class="categories"><div class="wrap">
  <h2 class="sec-title">Shop <b>Categories</b><span class="rule"></span></h2>
  <div class="cat-wrap">
    <div class="cat-feature"><div class="name">Novelty Sunglasses</div>
      <div class="ph" role="img" aria-label="Child wearing pink novelty sunglasses" style="background:linear-gradient(160deg,#f6d9e2,#f0a6bd)"></div></div>
    <div class="cat-grid">
      <div class="cat"><div class="ph" role="img" aria-label="Candy jars on a buffet table" style="background:linear-gradient(135deg,#3a2030,#e0606a)"></div><span class="label">Candy Buffet</span></div>
      <div class="cat"><div class="ph" role="img" aria-label="Party leggings and tights" style="background:linear-gradient(135deg,#f4f4f4,#9a9a9a)"></div><span class="label">Lights</span></div>
      <div class="cat"><div class="ph" role="img" aria-label="Red carnival masks" style="background:linear-gradient(135deg,#fafafa,#d8505a)"></div><span class="label">Carnival</span></div>
      <div class="cat"><div class="ph" role="img" aria-label="Green holiday wreath" style="background:radial-gradient(circle,#fff 30%,#3c7a3a 60%,#fff 80%)"></div><span class="label">Assortments</span></div>
      <div class="cat"><div class="ph" role="img" aria-label="Green tinsel wreath" style="background:radial-gradient(circle,#fff 30%,#4a9a3a 60%,#fff 80%)"></div><span class="label">Birthday Party</span></div>
      <div class="cat"><div class="ph" role="img" aria-label="Glowing craft supplies" style="background:linear-gradient(135deg,#15182a,#3fb6c9 50%,#f2a52e)"></div><span class="label">Craft Supplies</span></div>
    </div>
  </div>
</div></section>

<section class="banners"><div class="wrap">
  <div class="banner"><div class="ph" role="img" aria-label="Glow stick bracelets and necklaces" style="background:linear-gradient(135deg,#14142a,#5a3fb0 40%,#e03a8a 70%,#f2d13a)"></div>
    <div class="label teal"><b>Back to School</b><span>Bright supplies ready for the new school year</span></div></div>
  <div class="banner"><div class="ph" role="img" aria-label="Christmas gnome decoration with red hat" style="background:linear-gradient(135deg,#2a5a3a,#c23a3a 55%,#f0e8e0)"></div>
    <div class="label orange"><b>Summer Crafts</b><span>Fun craft kits for kids of all ages this summer</span></div></div>
</div></section>

<section class="featured"><div class="wrap">
  <div class="head"><h2 class="sec-title">Featured <b>Products</b><span class="rule"></span></h2><div class="dots"><span class="on"></span><span></span></div></div>
  <div class="products">
    <div class="product"><div class="img ph" role="img" aria-label="Neon feather masks" style="background:linear-gradient(135deg,#f7f7f7,#e8b040)"></div>
      <h4>Neon Animal Print Sunglasses Party Assortment</h4><div class="price"><s>$4.00</s><b>$7.98</b></div><a class="btn">Shop Now</a></div>
    <div class="product"><div class="img ph" role="img" aria-label="Black and white treat bags" style="background:linear-gradient(135deg,#f7f7f7,#555)"></div>
      <h4>Personalized Large Bright Color Tote Bags</h4><div class="price"><s>$4.00</s><b>$7.98</b></div><a class="btn">Shop Now</a></div>
    <div class="product"><div class="img ph" role="img" aria-label="Colourful glasses assortment" style="background:linear-gradient(135deg,#f7f7f7,#c04a4a)"></div>
      <h4>Colorful Mini Beach Playsets</h4><div class="price"><b>$11.99</b></div><a class="btn">Shop Now</a></div>
    <div class="product"><div class="img ph" role="img" aria-label="Green star shaped tinsel wreath" style="background:radial-gradient(circle,#fff 25%,#3c8a3a 55%,#fff 75%)"></div>
      <h4>Inflatable Floating Flamingo Coasters</h4><div class="price"><s>$4.00</s><b>$7.98</b></div><a class="btn">Shop Now</a></div>
  </div>
</div></section>

<section class="shipping">
  <svg class="bg" width="1200" height="420" viewBox="0 0 1200 420"><polygon points="0,0 330,420 0,420" fill="#f2a52e"/><polygon points="1200,0 1200,420 870,420" fill="#4c9ea9"/><rect x="0" y="330" width="1200" height="90" fill="#4c9ea9"/></svg>
  <div class="ship-text"><h2>Free shipping on orders over $99</h2><p>this offer is valid on all our store items</p><a class="btn">Shop Now Products</a></div>
  <div class="features">
    <div class="feature"><svg width="38" height="38" viewBox="0 0 38 38"><path d="M4 18h7v16H4zM11 18l7-14c3 0 4 2 3 6l-1 5h11c2 0 3 2 2 4l-4 13H11" fill="none" stroke="#4c9ea9" stroke-width="2.5"/></svg><h5>100% GUARANTEED</h5><p>Lorem ipsum has been the standard dummy text ever since a printer took a galley.</p></div>
    <div class="feature"><svg width="44" height="38" viewBox="0 0 44 38"><path d="M2 8h24v20H2zM26 14h9l6 7v7H26" fill="none" stroke="#4c9ea9" stroke-width="2.5"/><circle cx="10" cy="30" r="4" fill="#fff" stroke="#4c9ea9" stroke-width="2.5"/><circle cx="34" cy="30" r="4" fill="#fff" stroke="#4c9ea9" stroke-width="2.5"/></svg><h5>FREE SHIPPING &amp; RETURN</h5><p>Lorem ipsum has been the standard dummy text ever since a printer took a galley.</p></div>
    <div class="feature"><svg width="38" height="38" viewBox="0 0 38 38"><path d="M6 22v-4a13 13 0 0 1 26 0v4" fill="none" stroke="#4c9ea9" stroke-width="2.5"/><rect x="4" y="20" width="7" height="11" rx="2" fill="#4c9ea9"/><rect x="27" y="20" width="7" height="11" rx="2" fill="#4c9ea9"/></svg><h5>24/7 SUPPORT</h5><p>Lorem ipsum has been the standard dummy text ever since a printer took a galley.</p></div>
  </div>
</section>

<footer class="footer"><div class="wrap">
  <div class="col">
    <div class="brand"><span class="dot"></span>Partyvale</div>
    <p>There are many variations of passages of lorem ipsum available, but the majority have suffered alteration in some form, by injected humour, or randomised words.</p>
    <a class="btn">About Us</a>
  </div>
  <div class="col">
    <h6>Contact Us</h6>
    <div class="contact-line"><svg width="14" height="16" viewBox="0 0 14 16"><path d="M7 15s5-5 5-9a5 5 0 0 0-10 0c0 4 5 9 5 9z" fill="#fff"/><circle cx="7" cy="6" r="2" fill="#4c9ea9"/></svg>48 Meadow Lark Road, Fernvale, OR 97001</div>
    <div class="contact-line"><svg width="14" height="14" viewBox="0 0 14 14"><path d="M3 1l3 3-2 2c1 2 2 3 4 4l2-2 3 3-2 2C5 13 1 9 1 3z" fill="#fff"/></svg>Tel: (555)-014-7890</div>
    <div class="contact-line"><svg width="14" height="12" viewBox="0 0 14 12"><rect x="1" y="1" width="12" height="10" fill="none" stroke="#fff" stroke-width="1.5"/><path d="M1 1l6 5 6-5" fill="none" stroke="#fff" stroke-width="1.5"/></svg>hello@partyvale.shop</div>
  </div>
  <div class="col">
    <h6>Sign Up Newsletter</h6>
    <p>Be the first to hear about new arrivals, sales and party ideas. Join our newsletter.</p>
    <div class="newsletter"><div class="field">Enter your email</div><a class="btn">Send</a></div>
  </div>
</div>
<div class="bottombar"><div class="wrap">
  <div>© 2017 Partyvale. All Rights Reserved. Terms of use | Privacy Policy</div>
  <nav><a class="active">Home</a><a>Party Supplies</a><a>Occasions &amp; Events</a><a>Toys &amp; Games</a><a>Crafts</a><a>Teacher Supplies</a><a>Wedding</a><a>Holidays</a><a>Sale</a></nav>
  <div class="up"><svg width="12" height="10"><path d="M1 8l5-6 5 6" fill="none" stroke="#fff" stroke-width="2"/></svg></div>
</div></div>
</footer>

</body>
</html>
```